Soap Company Looking To Design New Soap Scent Boxes

we are looking to create a soap box similar to pa grunwell. we would like the circle cut out on the top right corner of the box. we are looking for a design that will allow us to use different color base banners for different soap scents (like pa. grunwell). we want the soap name scents to be large and readable on the bottom banner (like pa.grunwell). we have included our brand figure (logo) and some previous older soap box designs that we were making before the brand figure. the box dims are attached.

```html
<!DOCTYPE html>
<html lang="en">
<head>
<meta charset="utf-8">
<title>Fern &amp; Tallow — Plumeria Soap Box Dieline</title>
<link rel="stylesheet" href="https://fonts.googleapis.com/css2?family=Arimo:wght@400;700&family=Bowlby+One&family=Josefin+Sans:wght@400;600;700&family=Roboto+Slab:wght@500&display=swap">
<style>
  :root {
    --white: #ffffff;
    --leaf: #307039;
    --wine: #861219;
    --cocoa: #220507;
    --kraft: #e1c5a9;
    --kraft-dark: #b29581;
    --scent-band: #bd6aa6;
    --cut: #29abe2;
    --fold: #ed1c24;
    --safe: #00a650;
    --dim-red: #e31e24;
    --ink: #1a1a1a;
    --label-card: #f2e6d8;
  }
  html, body {
    margin: 0;
    padding: 0;
    width: 920px;
    height: 1200px;
    overflow: hidden;
    background: var(--white);
  }
  .sheet {
    position: relative;
    width: 920px;
    height: 1200px;
  }
  .dieline { display: block; }
  .dim-label { font-family: "Arimo", sans-serif; font-weight: 700; font-size: 40px; fill: var(--dim-red); }
  .swatch-label { font-family: "Arimo", sans-serif; font-weight: 400; font-size: 19px; fill: var(--ink); }
  .legend-label { font-family: "Arimo", sans-serif; font-weight: 400; font-size: 42px; }
  .body-copy { font-family: "Josefin Sans", sans-serif; font-size: 15.5px; fill: var(--wine); }
  .pill-text { font-family: "Roboto Slab", serif; font-weight: 500; font-size: 11px; fill: var(--white); letter-spacing: 0.4px; }
  .pill-text--small { font-size: 7.6px; letter-spacing: 0.2px; }
  .scent-item { font-family: "Josefin Sans", sans-serif; font-size: 7.4px; fill: var(--wine); }
  .feature-label { font-family: "Arimo", sans-serif; font-weight: 700; font-size: 7.6px; fill: var(--white); letter-spacing: 0.6px; }
  .brand-name { font-family: "Josefin Sans", sans-serif; font-weight: 700; fill: var(--cocoa); }
  .brand-name--side { fill: var(--wine); }
  .tagline { font-family: "Josefin Sans", sans-serif; font-size: 12.5px; fill: var(--wine); }
  .product-kicker { font-family: "Josefin Sans", sans-serif; font-size: 19px; fill: var(--white); }
  .product-name { font-family: "Bowlby One", sans-serif; font-size: 42px; fill: var(--white); letter-spacing: 0.5px; }
  .net-weight { font-family: "Josefin Sans", sans-serif; font-size: 10.5px; fill: var(--white); }
</style>
</head>
<body>
<main class="sheet">
  <svg class="dieline" width="920" height="646" viewBox="0 0 1680 1180" xmlns="http://www.w3.org/2000/svg">
    <defs>
      <marker id="arrow-head" viewBox="0 0 10 10" refX="9" refY="5" markerWidth="7" markerHeight="7" orient="auto-start-reverse">
        <path d="M0,0 L10,5 L0,10" fill="none" stroke="#1a1a1a" stroke-width="1.6"/>
      </marker>
      <linearGradient id="kraft-tone" x1="0" y1="0" x2="1" y2="1">
        <stop offset="0" stop-color="#e6ccb2"/>
        <stop offset="1" stop-color="#dbbea1"/>
      </linearGradient>
      <radialGradient id="figure-tone" cx="0.5" cy="0.45" r="0.6">
        <stop offset="0" stop-color="#f2d35a"/>
        <stop offset="0.6" stop-color="#e8a81e"/>
        <stop offset="1" stop-color="#307039"/>
      </radialGradient>
    </defs>

    <!-- dimensions -->
    <g class="dimensions">
      <text class="dim-label" x="528" y="120" text-anchor="middle">3.125"</text>
      <text class="dim-label" x="783" y="120" text-anchor="middle">1.125"</text>
      <text class="dim-label" x="1040" y="120" text-anchor="middle">3.125"</text>
      <text class="dim-label" x="1297" y="120" text-anchor="middle">1.125"</text>
      <g stroke="#1a1a1a" stroke-width="2" marker-start="url(#arrow-head)" marker-end="url(#arrow-head)">
        <line x1="355" y1="153" x2="700" y2="153"/>
        <line x1="731" y1="153" x2="837" y2="153"/>
        <line x1="868" y1="153" x2="1214" y2="153"/>
        <line x1="1244" y1="153" x2="1350" y2="153"/>
        <line x1="1397" y1="395" x2="1397" y2="741"/>
      </g>
      <text class="dim-label" transform="translate(1430 568) rotate(90)" text-anchor="middle">3.125"</text>
    </g>

    <!-- colour swatches -->
    <g class="swatches">
      <rect x="1413" y="157" width="28" height="28" rx="8" fill="var(--white)" stroke="#888" stroke-width="1"/>
      <text class="swatch-label" x="1450" y="178">ffffff</text>
      <rect x="1413" y="191" width="28" height="28" rx="8" fill="var(--leaf)"/>
      <text class="swatch-label" x="1450" y="212">307039</text>
      <rect x="1413" y="225" width="28" height="28" rx="8" fill="var(--wine)"/>
      <text class="swatch-label" x="1450" y="246">861219</text>
      <rect x="1413" y="259" width="28" height="28" rx="8" fill="var(--cocoa)"/>
      <text class="swatch-label" x="1450" y="280">220507</text>
      <rect x="1413" y="293" width="28" height="28" rx="8" fill="var(--kraft)"/>
      <text class="swatch-label" x="1450" y="314">e1c5a9</text>
      <rect x="1413" y="327" width="28" height="28" rx="8" fill="var(--kraft-dark)"/>
      <text class="swatch-label" x="1450" y="348">b29581</text>
    </g>

    <!-- kraft stock -->
    <rect class="kraft-stock" x="254" y="157" width="1139" height="828" fill="url(#kraft-tone)"/>

    <!-- scent bands -->
    <rect class="scent-band scent-band--back" x="338" y="626" width="378" height="131" fill="var(--scent-band)"/>
    <path class="scent-band scent-band--front" fill="var(--scent-band)"
      d="M851,757 L851,636 q6,-6 12,0 t12,0 t12,0 t12,0 t12,0 t12,0 t12,0 t12,0 t12,0 t12,0 t12,0 t12,0 t12,0 t12,0 t12,0 t12,0 t12,0 t12,0 t12,0 t12,0 t12,0 t12,0 t12,0 t12,0 t12,0 t12,0 t12,0 t12,0 t12,0 t12,0 t12,0 t12,0 L1229,636 L1229,757 Z"/>

    <!-- back panel -->
    <g class="panel panel--back">
      <rect x="422" y="425" width="212" height="18" rx="9" fill="var(--wine)"/>
      <text class="pill-text" x="528" y="438" text-anchor="middle" textLength="196" lengthAdjust="spacingAndGlyphs">FERN &amp; TALLOW ARTISAN SOAP BAR</text>
      <text class="body-copy" text-anchor="middle">
        <tspan x="525" y="478">Our Bath Soaps collection are infused</tspan>
        <tspan x="525" y="496">with all-organic ingredients, including</tspan>
        <tspan x="525" y="514">Coconut Oil, Canola Oil, Soybean Oil,</tspan>
        <tspan x="525" y="532">Shea Butter, Water, Sodium Hydroxide (Lye)</tspan>
        <tspan x="525" y="550">Olive Pomace Oil, Sunflower Oil, Fragrance.</tspan>
        <tspan x="525" y="568">This is nature in a bar!</tspan>
      </text>
      <g class="feature-icons" fill="none" stroke="var(--white)" stroke-width="2" stroke-linecap="round" stroke-linejoin="round">
        <path d="M424,690 L424,660 M430,688 L430,652 M436,688 L436,650 M442,690 L442,656 M424,680 Q420,690 430,692 L442,692 Q448,688 448,676"/>
        <circle cx="435" cy="680" r="4"/>
        <path d="M509,682 L522,682 Q532,686 544,678 M509,690 L540,690 Q552,684 556,672"/>
        <path d="M531,675 L531,660 M531,662 Q520,652 516,662 Q524,668 531,666 M531,662 Q542,652 546,662 Q538,668 531,666 M531,656 Q527,648 531,644 Q535,648 531,656"/>
        <rect x="610" y="660" width="26" height="22" rx="8" transform="rotate(-35 623 671)"/>
        <circle cx="638" cy="655" r="4"/>
        <circle cx="641" cy="686" r="3"/>
      </g>
      <text class="feature-label" x="435" y="708" text-anchor="middle">HANDMADE</text>
      <text class="feature-label" text-anchor="middle"><tspan x="531" y="708">ALL-NATURAL</tspan><tspan x="531" y="717">INGREDIENTS</tspan></text>
      <text class="feature-label" text-anchor="middle"><tspan x="627" y="708">VARIETY OF</tspan><tspan x="627" y="717">SOAP SCENTS</tspan></text>
    </g>

    <!-- left side panel -->
    <g class="panel panel--scents">
      <rect x="735" y="425" width="98" height="255" rx="6" fill="var(--label-card)" opacity="0.8"/>
      <rect x="735" y="408" width="98" height="17" rx="8.5" fill="var(--wine)"/>
      <text class="pill-text pill-text--small" x="784" y="419.5" text-anchor="middle" textLength="84" lengthAdjust="spacingAndGlyphs">AVAILABLE SCENTS</text>
      <text class="scent-item" text-anchor="middle">
        <tspan x="784" y="441">CEDARWOOD TEA TREE</tspan>
        <tspan x="784" y="454.5">CHARCOAL ALOE</tspan>
        <tspan x="784" y="468">COOL WATER</tspan>
        <tspan x="784" y="481.5">DEAD SEA SCRUB</tspan>
        <tspan x="784" y="495">EUCALYPTUS ALOE</tspan>
        <tspan x="784" y="508.5">HYDRANGEA</tspan>
        <tspan x="784" y="522">JASMINE LIME SCRUB</tspan>
        <tspan x="784" y="535.5">MANGO PAPAYA</tspan>
        <tspan x="784" y="549">MOUNTAIN AIR</tspan>
        <tspan x="784" y="562.5">NAG CHAMPA</tspan>
        <tspan x="784" y="576">PLUMERIA</tspan>
        <tspan x="784" y="589.5">POMEGRANATE CHERRY</tspan>
        <tspan x="784" y="603">RASPBERRY RUSH</tspan>
        <tspan x="784" y="616.5">RASPBERRY VANILLA</tspan>
        <tspan x="784" y="630">SANDALWOOD ROSE</tspan>
        <tspan x="784" y="643.5">TANGERINE GRAPEFRUIT</tspan>
        <tspan x="784" y="657">WILD PASSION</tspan>
        <tspan x="784" y="670.5">WILDFLOWERS</tspan>
      </text>
      <text class="brand-name brand-name--side" x="784" y="716" text-anchor="middle" font-size="14">Fern &amp; Tallow</text>
    </g>

    <!-- front panel -->
    <g class="panel panel--front">
      <ellipse cx="1036" cy="488" rx="56" ry="62" fill="url(#figure-tone)" role="img" aria-label="Brand figure illustration: hooded girl with blonde hair in green cloak on a gold oval"/>
      <text class="brand-name" x="1038" y="590" text-anchor="middle" font-size="34">Fern &amp; Tallow</text>
      <circle class="thumb-cutout" cx="1152" cy="448" r="36" fill="none" stroke="var(--cut)" stroke-width="1.3"/>
      <text class="product-kicker" x="1040" y="666" text-anchor="middle">Cold Pressed Artisan Soap</text>
      <text class="product-name" x="1040" y="706" text-anchor="middle">PLUMERIA</text>
      <text class="net-weight" x="1040" y="728" text-anchor="middle">Net Wt. 5oz (140g)</text>
    </g>

    <!-- right side panel -->
    <g class="panel panel--tagline">
      <g class="lotus" fill="none" stroke="var(--wine)" stroke-width="1.6">
        <path d="M1298,416 Q1284,436 1298,462 Q1312,436 1298,416 Z"/>
        <path d="M1296,462 Q1276,452 1272,428 Q1288,438 1296,462"/>
        <path d="M1300,462 Q1320,452 1324,428 Q1308,438 1300,462"/>
        <path d="M1268,450 Q1282,468 1298,466 Q1314,468 1328,450"/>
      </g>
      <text class="tagline" text-anchor="middle">
        <tspan x="1298" y="493">REJUVENATE</tspan>
        <tspan x="1298" y="506">YOUR MIND</tspan>
        <tspan x="1298" y="519">BODY AND SOUL</tspan>
      </text>
      <g class="care-icons" fill="none" stroke="var(--wine)" stroke-width="2">
        <path d="M1260,730 L1268,716 L1276,730 Z"/>
        <path d="M1292,732 Q1290,718 1300,714 Q1310,718 1308,732 Z"/>
        <path d="M1324,718 L1338,718 L1336,734 L1326,734 Z M1330,710 L1330,714"/>
      </g>
    </g>

    <!-- cutting line -->
    <path class="cut-line" fill="none" stroke="var(--cut)" stroke-width="1.4"
      d="M338,370 L338,243 L325,243 L325,202 Q325,168 360,168 L695,168 Q730,168 730,202 L730,243 L716,243 L716,275 L825,275 L840,345 L855,360 L1225,360 L1240,345 L1250,275 L1380,275 L1380,780 L1362,800 L1346,860 L1240,860 L1240,938 Q1240,972 1206,972 L872,972 Q838,972 838,938 L838,860 L732,860 L732,800 L716,780 L716,770 L338,770 L290,757 L262,745 L262,385 L290,380 Z"/>

    <!-- folding lines -->
    <g class="fold-lines" fill="none" stroke="var(--fold)" stroke-width="1.2">
      <line x1="338" y1="380" x2="1365" y2="380"/>
      <line x1="338" y1="757" x2="1365" y2="757"/>
      <line x1="338" y1="380" x2="338" y2="757"/>
      <line x1="716" y1="290" x2="716" y2="850"/>
      <line x1="851" y1="380" x2="851" y2="960"/>
      <line x1="1229" y1="380" x2="1229" y2="960"/>
      <line x1="1365" y1="290" x2="1365" y2="770"/>
      <line x1="338" y1="243" x2="716" y2="243"/>
      <line x1="851" y1="890" x2="1229" y2="890"/>
      <path d="M338,243 L338,210 Q338,183 365,183 L690,183 Q716,183 716,210 L716,243"/>
      <path d="M716,290 L820,290 L835,350 L851,380"/>
      <path d="M1229,380 L1245,350 L1258,290 L1365,290"/>
      <path d="M716,757 L735,790 L748,848 L838,848"/>
      <path d="M1229,757 L1245,790 L1258,848 L1365,848 L1365,770"/>
      <path d="M851,890 L851,930 Q851,958 878,958 L1202,958 Q1229,958 1229,930 L1229,890"/>
      <path d="M338,395 L280,398 L280,740 L338,745"/>
    </g>

    <!-- safe zones -->
    <g class="safe-zones" fill="none" stroke="var(--safe)" stroke-width="1.2">
      <rect x="354" y="199" width="346" height="30" rx="10"/>
      <rect x="354" y="258" width="346" height="106"/>
      <rect x="354" y="395" width="346" height="346"/>
      <rect x="731" y="395" width="105" height="346"/>
      <rect x="867" y="395" width="347" height="346"/>
      <rect x="1244" y="395" width="106" height="346"/>
      <path d="M731,305 L815,305 L828,364 L731,364 Z"/>
      <path d="M1350,305 L1268,305 L1252,364 L1350,364 Z"/>
      <path d="M738,772 L836,772 L836,832 L752,832 Z"/>
      <path d="M1244,772 L1342,772 L1328,832 L1244,832 Z"/>
      <rect x="867" y="772" width="347" height="106"/>
      <rect x="867" y="908" width="347" height="30" rx="10"/>
      <path d="M296,410 L323,400 L323,733 L296,726 Z"/>
    </g>

    <!-- line legend -->
    <g class="line-legend">
      <circle cx="355" cy="1116" r="27" fill="var(--cut)"/>
      <text class="legend-label" x="390" y="1129" fill="var(--cut)">Cutting Line</text>
      <circle cx="725" cy="1116" r="27" fill="var(--fold)"/>
      <text class="legend-label" x="757" y="1129" fill="var(--fold)">Folding line</text>
      <circle cx="1098" cy="1116" r="27" fill="var(--safe)"/>
      <text class="legend-label" x="1135" y="1131" fill="var(--safe)">Safe zone</text>
    </g>
  </svg>
</main>
</body>
</html>
```